Open Window; Sunrise Table, River Walk Rack Card

We want an additional 2 page (front and page) 3.67" x 8.5" rack card. This rack card is now the 2nd of the series . The first one is already completed/finalized and attached (Sunrise Table River Walk Rack Card PDF).
Use the text on the word document for the included Open Window Rack card. Please use the Sunrise Table River Walk Rack card as the template to mimic. We would like all subsequent rack cards to have a similar look and feel.
The document is for older readers. Do not put text over graphics and keep it simple and easy to read with high contrast.
We want some very simple design element(s) incorporated that convey Native American communities or heritage. But NO headdress, teepee graphics, etc. At the top, of the first page we would like a collage of healthy food images. This can include fish, chicken, fresh vegetables, berries, brown rice, etc. Please remember to include the funding statement - it can be in a very small font 6/7 point. For more information about our project, please visit https://pelmorvo.org/kite-lane/

```html
<!DOCTYPE html>
<html lang="en">
<head>
<meta charset="utf-8">
<title>Sunrise Table River Walk Rack Card</title>
<link href="https://fonts.googleapis.com/css2?family=Oswald:wght@500;700&family=Source+Sans+3:ital,wght@0,400;0,600;0,700;1,700&display=swap" rel="stylesheet">
<style>
:root{
  --backdrop:#7f7f83;
  --paper:#f7f6f2;
  --maroon:#6b1f1f;
  --teal:#3a8f97;
  --rust:#b4584a;
  --ink:#262626;
  --band-soft:#c9d6d6;
}
*{box-sizing:border-box;margin:0;padding:0}
html,body{width:1154px;height:1200px;overflow:hidden}
body{background:var(--backdrop);font-family:"Source Sans 3",Arial,sans-serif;color:var(--ink);position:relative}
.card{position:absolute;top:70px;width:480px;height:1044px;background:var(--paper);box-shadow:0 6px 14px rgba(0,0,0,.35);display:flex;flex-direction:column;overflow:hidden}
.card--front{left:82px}
.card--back{left:590px;top:76px}
.photo{flex:none}
.food-collage{height:178px;background:linear-gradient(100deg,#5b6b3a 0%,#a8a58a 35%,#e2ddd2 55%,#d98a5a 80%,#8a3a2a 100%)}
.title{font-family:Oswald,Impact,sans-serif;font-weight:700;text-transform:uppercase;text-align:center;line-height:.98}
.card--front .title{font-size:50px;padding:8px 16px 0}
.title .line-a{color:var(--maroon);display:block}
.title .line-b{color:var(--teal);display:block}
.front-body{padding:10px 22px 0}
.intro{font-weight:700;font-size:15.5px;line-height:1.2}
.subhead{font-weight:700;font-size:17px;color:var(--teal);margin:12px 0 6px}
.subhead em{font-style:normal;color:var(--rust)}
.checklist{list-style:none}
.checklist li{position:relative;padding-left:26px;font-weight:700;font-size:15px;line-height:1.18;margin-bottom:6px}
.checklist li svg{position:absolute;left:0;top:2px}
.checklist q{font-style:italic;quotes:"\201C" "\201D"}
.closing{color:var(--rust);font-weight:700;font-size:17px;line-height:1.15;margin-top:10px}
.pattern-band{height:20px;background:var(--band-soft);flex:none}
.card--front .pattern-band{margin-top:auto}
.talk-band{background:var(--maroon);color:#fff;font-weight:700;font-size:12.5px;text-transform:uppercase;text-align:center;line-height:1.25;padding:8px 14px;flex:none}
.quote-area{height:184px;display:flex;flex:none}
.quote{padding:18px 0 0 22px;width:260px}
.quote p{font-weight:700;font-size:14.5px;line-height:1.2;position:relative;padding-left:20px}
.quote p::before{content:"\201C";position:absolute;left:-2px;top:-10px;font-size:34px;color:var(--teal);font-family:Georgia,serif}
.quote p::after{content:"\201D";font-size:34px;color:var(--teal);font-family:Georgia,serif;line-height:0;vertical-align:-12px}
.quote cite{display:block;font-style:normal;font-weight:600;font-size:11px;margin-top:8px}
.berries{flex:1;margin:24px 0 0;background:radial-gradient(circle at 55% 60%,#7a1d3a 0%,#a33a4d 35%,#5a3b6e 60%,rgba(247,246,242,0) 80%)}
.footer{background:var(--teal);color:#fff;flex:none}
.card--front .footer{height:60px;padding:10px 22px;font-weight:700;font-size:15px}

.card--back .title{font-size:35px;padding:26px 16px 14px;white-space:nowrap}
.card--back .title span{display:inline}
.recipe-top{display:flex;padding:0 20px;gap:10px}
.recipe-name{width:140px;flex:none}
.recipe-name h3{color:var(--teal);font-weight:700;font-size:16px;line-height:1.15}
.stew{height:106px;margin-top:10px;border-radius:50% 50% 46% 46%;background:radial-gradient(ellipse at 50% 40%,#c9a77a 0%,#8c5a33 55%,#5a3418 100%)}
.ingredients{list-style:none;flex:1}
.ingredients li{position:relative;padding-left:24px;font-weight:700;font-size:15px;line-height:1.2;margin-bottom:7px}
.ingredients li svg{position:absolute;left:0;top:2px}
.method{padding:14px 20px 0;font-weight:700;font-size:15px;line-height:1.22}
.yield{color:var(--rust);font-weight:700;font-size:15px;padding:0 20px}
.elders{background:var(--teal);color:#fff;margin-top:18px;height:112px;display:flex;align-items:center;padding:0 20px;gap:18px;flex:none}
.tree-mark{width:76px;height:76px;flex:none;background:rgba(255,255,255,.22);border-radius:6px}
.elders p{font-weight:700;font-size:14.5px;line-height:1.2}
.card--back .pattern-band{margin-top:18px}
.more-info{text-align:center;padding:12px 24px 0}
.more-info h4{color:var(--teal);font-weight:700;font-size:14px;margin-bottom:10px}
.link-label{font-weight:700;font-size:13.5px;color:var(--maroon);margin-top:12px}
.link-label b{color:var(--rust)}
.link-pill{display:block;background:var(--maroon);color:#fff;font-weight:700;font-size:15px;border-radius:18px;padding:7px 0;margin:8px 0 0}
.brand-row{display:flex;align-items:flex-end;margin-top:auto;height:112px;flex:none}
.brand{display:flex;align-items:center;gap:8px;padding:0 0 16px 22px;width:230px}
.brand-dot{width:34px;height:34px;border-radius:50%;background:var(--teal);flex:none}
.brand span{font-weight:700;font-size:18px;color:var(--teal);line-height:1.05}
.produce{flex:1;height:150px;margin-top:-40px;background:radial-gradient(ellipse at 60% 60%,#c23a22 0%,#d98a2a 30%,#6d8a2e 55%,rgba(247,246,242,0) 78%)}
.card--back .footer{height:80px;padding:9px 180px 0 20px;font-size:7px;line-height:1.3}
</style>
</head>
<body>

<article class="card card--front">
  <div class="photo food-collage" role="img" aria-label="Collage of healthy food: greens, brown rice, berries and baked salmon with lemon"></div>
  <h1 class="title"><span class="line-a">Sunrise Table</span><span class="line-b">River Walk</span></h1>
  <div class="front-body">
    <p class="intro">Making small changes in what and how you eat can make you feel better and stay healthier longer. Healthy food choices may be good for your brain, energy, mood, and health.</p>
    <h2 class="subhead">Little changes that make a <em>big difference:</em></h2>
    <ul class="checklist">
      <li><svg width="16" height="16" viewBox="0 0 16 16"><rect x="1" y="3" width="11" height="11" fill="none" stroke="#3a8f97" stroke-width="1.5"/><path d="M3 8l3 3 8-9" fill="none" stroke="#3a8f97" stroke-width="2"/></svg>Start today!</li>
      <li><svg width="16" height="16" viewBox="0 0 16 16"><rect x="1" y="3" width="11" height="11" fill="none" stroke="#3a8f97" stroke-width="1.5"/><path d="M3 8l3 3 8-9" fill="none" stroke="#3a8f97" stroke-width="2"/></svg>Write down what, when, and how much you eat for three days</li>
      <li><svg width="16" height="16" viewBox="0 0 16 16"><rect x="1" y="3" width="11" height="11" fill="none" stroke="#3a8f97" stroke-width="1.5"/><path d="M3 8l3 3 8-9" fill="none" stroke="#3a8f97" stroke-width="2"/></svg>Set SMART goals (Specific, Measurable, Attainable, Relevant &amp; Timebound), like: <q>I will eat one piece of fruit at breakfast three times this week.</q></li>
      <li><svg width="16" height="16" viewBox="0 0 16 16"><rect x="1" y="3" width="11" height="11" fill="none" stroke="#3a8f97" stroke-width="1.5"/><path d="M3 8l3 3 8-9" fill="none" stroke="#3a8f97" stroke-width="2"/></svg>Make just 1 or 2 changes at a time until they become a habit</li>
      <li><svg width="16" height="16" viewBox="0 0 16 16"><rect x="1" y="3" width="11" height="11" fill="none" stroke="#3a8f97" stroke-width="1.5"/><path d="M3 8l3 3 8-9" fill="none" stroke="#3a8f97" stroke-width="2"/></svg>Focus more on eating healthy food versus not eating unhealthy food</li>
      <li><svg width="16" height="16" viewBox="0 0 16 16"><rect x="1" y="3" width="11" height="11" fill="none" stroke="#3a8f97" stroke-width="1.5"/><path d="M3 8l3 3 8-9" fill="none" stroke="#3a8f97" stroke-width="2"/></svg>Make a game plan for the times you get tempted to eat unhealthy foods</li>
      <li><svg width="16" height="16" viewBox="0 0 16 16"><rect x="1" y="3" width="11" height="11" fill="none" stroke="#3a8f97" stroke-width="1.5"/><path d="M3 8l3 3 8-9" fill="none" stroke="#3a8f97" stroke-width="2"/></svg>Involve the whole family in setting goals</li>
      <li><svg width="16" height="16" viewBox="0 0 16 16"><rect x="1" y="3" width="11" height="11" fill="none" stroke="#3a8f97" stroke-width="1.5"/><path d="M3 8l3 3 8-9" fill="none" stroke="#3a8f97" stroke-width="2"/></svg>Name your main reason to eat healthier and feel better, like <q>More energy to go to church and tribal cultural events.</q></li>
    </ul>
    <p class="closing">Making small, practical changes can help you achieve your health goals.</p>
  </div>
  <div class="pattern-band" role="img" aria-label="Band of traditional chevron pattern"></div>
  <div class="talk-band">Talk to your doctor about healthier eating<br>to make you feel better and stay healthier longer</div>
  <div class="quote-area">
    <blockquote class="quote">
      <p>When it comes to traditional foods, for me it’s something more than just food, it’s my heritage</p>
      <cite>Marla Tenwick (Desert River Nation)</cite>
    </blockquote>
    <div class="photo berries" role="img" aria-label="Bowl of spilling mixed berries"></div>
  </div>
  <footer class="footer">www.pelmorvo.com</footer>
</article>

<article class="card card--back">
  <h2 class="title"><span class="line-a">Make this </span><span class="line-b">at home</span></h2>
  <div class="recipe-top">
    <div class="recipe-name">
      <h3>O’odham White Tepary Bean Stew</h3>
      <div class="photo stew" role="img" aria-label="Wooden bowl of white bean stew"></div>
    </div>
    <ul class="ingredients">
      <li><svg width="16" height="16" viewBox="0 0 16 16"><rect x="1" y="3" width="11" height="11" fill="none" stroke="#3a8f97" stroke-width="1.5"/><path d="M3 8l3 3 8-9" fill="none" stroke="#3a8f97" stroke-width="2"/></svg>1 cup dried tepary beans, rinsed &amp; picked through (substitute Navy Beans or Great Northern beans)</li>
      <li><svg width="16" height="16" viewBox="0 0 16 16"><rect x="1" y="3" width="11" height="11" fill="none" stroke="#3a8f97" stroke-width="1.5"/><path d="M3 8l3 3 8-9" fill="none" stroke="#3a8f97" stroke-width="2"/></svg>10 cups of water</li>
      <li><svg width="16" height="16" viewBox="0 0 16 16"><rect x="1" y="3" width="11" height="11" fill="none" stroke="#3a8f97" stroke-width="1.5"/><path d="M3 8l3 3 8-9" fill="none" stroke="#3a8f97" stroke-width="2"/></svg>1 tsp. salt</li>
      <li><svg width="16" height="16" viewBox="0 0 16 16"><rect x="1" y="3" width="11" height="11" fill="none" stroke="#3a8f97" stroke-width="1.5"/><path d="M3 8l3 3 8-9" fill="none" stroke="#3a8f97" stroke-width="2"/></svg>1 lb. oxtails, beef short ribs, deer, rabbit, or chicken</li>
    </ul>
  </div>
  <p class="method">Put beans, water, and salt in a stockpot. Bring to a boil, reduce heat and simmer, covered, for one hour and a half. Add meat to the bean mixture, cover and cook for one more hour, or until beans are tender and meat is falling off the bone. If using a crockpot, place water and all other ingredients in the pot, cover, and set to high. Cook for 8 hours or until the meat is falling off the bone and the beans are tender.</p>
  <p class="yield">Makes 8 – 10 cups</p>
  <div class="elders">
    <div class="tree-mark" role="img" aria-label="Simple line icon of trees"></div>
    <p>Elders are our keepers of traditional knowledge about food and ways of life. You play an important role in sharing this knowledge with younger generations.</p>
  </div>
  <div class="pattern-band" role="img" aria-label="Band of traditional chevron pattern"></div>
  <section class="more-info">
    <h4>For More Information</h4>
    <p class="link-label"><b>About Goal Setting</b> Guild of Food and Wellness</p>
    <span class="link-pill">https://go.tavrel.org/GoalVideo</span>
    <p class="link-label"><b>Harrowgate Medicine</b></p>
    <span class="link-pill">https://go.tavrel.org/SmartGoals</span>
  </section>
  <div class="brand-row">
    <div class="brand"><i class="brand-dot"></i><span>Open Window Resource Center</span></div>
    <div class="photo produce" role="img" aria-label="Basket of fresh vegetables: tomatoes, peppers, greens"></div>
  </div>
  <footer class="footer">This product is supported by the Office of Public Wellness as part of a financial assistance award totaling $000,000 with 100 percent funded by the Office. The contents are those of the author(s) and do not necessarily represent the official views of, nor an endorsement, by the Office or the Government.</footer>
</article>

</body>
</html>
```